Shop Image re-design

Hi,

We are a company who operate several convenience stores around Northern Ireland, and are currently trading under a generic name of 'lorn'. We have made a decision to re-brand the stores under the name of "The Quiet Fox", and will start the process by intially trialling the new look by converting our flag ship, and busiest shop to evaluate the results. The stops main focus is on fresh convenience foods - Coffee,sandwichs,fruit,fresh pastries,chilled drinks & juices etc but we also sell the usual items you would expect such as newspapers, magazines, greeting cards, snacks, confectionery etc

This store is situated in a busy hospital and we serve upward of 25,000 customers a week - doctors, nurses, support staff,patients and visitors all of whom come from a wide cross section of society so the design and style of the new rebranding will have to be SPECTACULARY good to win!

The Design we are looking for must be very Professional, stylish, modern, eye catching and yet still display a fun,welcoming and friendly image to our customers.

I have Included some image files of the current look and feel of the branding in the store, these include the outside signage, internal graphics and point of sale material. Its a good image and brand we have at the moment but I want something EXCEPTIONAL that will make us stand out from other retailers, and be memorable to the customers!

Some things to consider...

The main design should be for the outside signage (see image attached for shape, position and general size). The design should not be to cluttered, and the name as mentioned before will be "the quiet fox" but additionally for this store the term "hospital shop" should also be added underneath the main title,but in a much smaller size to the overall name.In other shops we will propably change the term "hospital shop" to "newsagents" where this is more appropriate, but we will redesign this when we come to convert these stores in due course.

I think we should still display some general 'product' images on the outside signage as is currently the case, and if any are included the images should be of a very high resolution and quality, and make you want to eat it!
Although Im suggesting we should keep some sort of images please donot stop your creative processes, if you think something looks good without them...please submit!

The overall 'feel' and style of the outside sign should flow through into the shop with the internal '3d' signage being of a simalar style as well as the point of sale graphics. In submitting for the internal signage please just do so in a 2d format. (see attached images)

The point of sale materal (shelf 'barkers' and a4 posters), that we use around the shop are of a pre-printed coloured card nature that the managers can run through a laser printer to produce store-specific special offers etc. (see attached images)

We are very excited about this re-branding, as we have used artmarketo before to help us design our company stationery etc., with great results! We therefore hope all you talented designers out there can help us make it a reality... so let your creative juices flow we want something very original!

Thanks,

Rupert.

Target Market(s)

As described in the above brief...
It is worth noting that our stores do not operate in 'value focused' enviroment, we are more more concerned with quality of product and speed and quality of service.

Requirements
Must have
• See detailed design brief above.
Nice to have
• It would be good to have a theme that we can transfer across the store onto uniforms, carrier bags, coffee cups and still fits into the overall 'brand' image
Should not have
• Cartoons or childish style designs or graphics!

```html
<!DOCTYPE html>
<html lang="en">
<head>
<meta charset="utf-8">
<title>The Quiet Fox – A4 Poster Card</title>
<link rel="stylesheet" href="https://fonts.googleapis.com/css2?family=Baloo+2:wght@800&display=swap">
<style>
  :root {
    --paper: #fbf7dc;
    --brand-yellow: #f2c318;
    --brand-black: #141414;
  }
  html, body {
    margin: 0;
    padding: 0;
    overflow: hidden;
    background: var(--paper);
  }
  .poster {
    position: relative;
    width: 851px;
    height: 1200px;
    background: var(--paper);
    overflow: hidden;
  }
  .header-swoosh {
    position: absolute;
    top: 0;
    left: 0;
    width: 851px;
    height: 340px;
  }
  .swoosh-yellow { fill: var(--brand-yellow); }
  .swoosh-black { fill: var(--brand-black); }
  .brand-lockup {
    position: absolute;
    top: 34px;
    left: 572px;
    width: 250px;
    display: flex;
    align-items: center;
    gap: 10px;
  }
  .brand-mark {
    flex: none;
    width: 18px;
    height: 18px;
    border-radius: 50%;
    background: var(--brand-black);
  }
  .brand-name {
    margin: 0;
    font-family: "Baloo 2", sans-serif;
    font-weight: 800;
    font-size: 40px;
    line-height: 0.95;
    color: var(--brand-black);
  }
</style>
</head>
<body>
  <main class="poster">
    <svg class="header-swoosh" viewBox="0 0 851 340" aria-hidden="true">
      <path class="swoosh-yellow" d="M0,0 H851 V318 C820,190 720,60 520,14 H0 Z"/>
      <path class="swoosh-black" d="M851,292 C826,200 770,130 700,110 C760,150 800,200 820,250 C835,270 845,285 851,292 Z"/>
      <path class="swoosh-black" d="M851,292 C832,210 790,160 730,125 C800,150 840,200 851,230 Z"/>
    </svg>
    <div class="brand-lockup">
      <span class="brand-mark"></span>
      <h1 class="brand-name">The Quiet Fox</h1>
    </div>
  </main>
</body>
</html>
```